Business Card for IT company

I need a high tech looking business card using our logo. I prefer something clean and modern.

Target Market(s)

Buyers of IT hardware and software, IT Techies who are key influencers

Industry/Entity Type

Business

```html
<!DOCTYPE html>
<html lang="en">
<head>
<meta charset="utf-8">
<title>Norvale Consulting – Business Card</title>
<link rel="stylesheet" href="https://fonts.googleapis.com/css2?family=Open+Sans:wght@300;400;600;700&display=swap">
<style>
  :root {
    --page: #e9e9e7;
    --charcoal: #2a2a2b;
    --charcoal-deep: #151516;
    --charcoal-light: #3a3a3c;
    --green: #3db34a;
    --green-dark: #2a8f36;
    --paper: #ffffff;
    --ink: #3b3b3d;
    --ink-soft: #6b6b6e;
    --white: #ffffff;
  }
  * { margin: 0; padding: 0; box-sizing: border-box; }
  html, body {
    width: 1200px; height: 1024px; overflow: hidden;
    background: var(--page);
    font-family: "Open Sans", Arial, sans-serif;
  }
  .sheet {
    width: 1200px; height: 1024px;
    display: flex; flex-direction: column; align-items: center; justify-content: center;
    gap: 72px;
  }
  .card {
    position: relative;
    width: 700px; height: 400px;
    overflow: hidden;
    box-shadow: 0 10px 28px rgba(0,0,0,0.18);
  }

  /* Front */
  .card-front {
    background: linear-gradient(135deg, var(--charcoal-light) 0%, var(--charcoal) 45%, var(--charcoal-deep) 100%);
  }
  .front-pattern {
    position: absolute; inset: 0;
    background:
      repeating-linear-gradient(-35deg, rgba(255,255,255,0.035) 0 34px, rgba(0,0,0,0.06) 34px 68px);
  }
  .front-band {
    position: absolute; left: -60px; right: -60px; top: 130px; height: 140px;
    background: linear-gradient(90deg, rgba(255,255,255,0.02), rgba(255,255,255,0.07), rgba(255,255,255,0.02));
    transform: rotate(-35deg);
  }
  .front-brand {
    position: absolute; left: 50%; top: 50%;
    transform: translate(-50%, -50%);
    display: flex; align-items: center; gap: 14px;
  }
  .brand-mark {
    width: 22px; height: 22px; background: var(--green);
  }
  .brand-name {
    font-weight: 300; letter-spacing: 3px; text-transform: uppercase;
  }
  .front-brand .brand-name { color: var(--white); font-size: 34px; }

  /* Back */
  .card-back { background: var(--paper); }
  .back-edge {
    position: absolute; left: 0; top: 0; bottom: 0; width: 58px;
    background: var(--charcoal);
  }
  .back-edge::after {
    content: ""; position: absolute; right: -10px; top: 0; bottom: 0; width: 10px;
    background: var(--green);
  }
  .back-brand {
    position: absolute; right: 48px; top: 48px;
    display: flex; align-items: center; gap: 12px;
  }
  .back-brand .brand-name { color: var(--ink); font-size: 30px; }
  .person {
    position: absolute; left: 112px; top: 178px;
  }
  .person-name {
    color: var(--green-dark); font-weight: 700; font-size: 34px; line-height: 1.1;
  }
  .person-role {
    color: var(--ink-soft); font-size: 17px; margin-top: 4px;
  }
  .contact {
    position: absolute; left: 112px; top: 272px;
    list-style: none; color: var(--ink); font-size: 17px; line-height: 1.65;
  }
  .contact-label { color: var(--green-dark); font-weight: 600; display: inline-block; width: 22px; }
</style>
</head>
<body>
<main class="sheet">
  <section class="card card-front">
    <div class="front-pattern" role="img" aria-label="Repeating diagonal company-name pattern in dark grey tones"></div>
    <div class="front-band"></div>
    <div class="front-brand">
      <span class="brand-mark"></span>
      <span class="brand-name">Norvale Consulting</span>
    </div>
  </section>

  <section class="card card-back">
    <div class="back-edge"></div>
    <div class="back-brand">
      <span class="brand-mark"></span>
      <span class="brand-name">Norvale Consulting</span>
    </div>
    <div class="person">
      <p class="person-name">Jordan Pike</p>
      <p class="person-role">General Manager</p>
    </div>
    <ul class="contact">
      <li><span class="contact-label">P</span>555.000.4417</li>
      <li><span class="contact-label">E</span>jordan@norvale.com</li>
      <li><span class="contact-label">W</span>www.norvale.com</li>
    </ul>
  </section>
</main>
</body>
</html>
```